Business Card Design Project

We need a business card for our IT services provider business. We provide services to small and medium business, and would like something that reflects the color scheme / branding on our recently updated website - www.tallobrix.com.au

The card type we have chosen is a matte laminated double sided configuration at 86mm x 54mm on 350 GSM cardboard.
Updates

Target Market(s)

Small and Medium Business owners

Industry/Entity Type

Business

Requirements
Must have
• *Details on all cards*

Company Name: Tallobrix Pty Ltd
ABN: 52 683 914 207
Address: 47-49 Pembury Street, Ashcombe Vale, Victoria 3172
Phone: 1300 GRAB UP
Fax: 03 9417 6258
Website: www.tallobrix.com.au
Logo/Handprint Icon

*Person Specific*

```html
<!DOCTYPE html>
<html lang="en">
<head>
<meta charset="utf-8">
<title>Tallobrix Business Card</title>
<link rel="stylesheet" href="https://fonts.googleapis.com/css2?family=Roboto+Condensed:wght@400;700&display=swap">
<style>
  :root {
    --page-bg: #e9eaec;
    --card-white: #ffffff;
    --brand-blue: #1e6db3;
    --brand-blue-deep: #1a5596;
    --watermark-grey: #dfe0e2;
    --ink: #3a3a3a;
    --ink-light: #ffffff;
  }
  * { box-sizing: border-box; margin: 0; padding: 0; }
  html, body {
    width: 1141px;
    height: 1200px;
    overflow: hidden;
    background: var(--page-bg);
    font-family: "Roboto Condensed", "Arial Narrow", sans-serif;
  }
  .sheet {
    width: 1141px;
    height: 1200px;
    display: flex;
    flex-direction: column;
    align-items: center;
    justify-content: center;
    gap: 40px;
  }
  .card {
    position: relative;
    width: 860px;
    height: 540px;
    box-shadow: 0 2px 6px rgba(0,0,0,0.12);
    overflow: hidden;
  }
  .card--front { background: var(--card-white); }
  .card--back { background: var(--brand-blue); }

  .watermark {
    position: absolute;
    border-radius: 46% 46% 40% 40%;
  }
  .card--front .watermark {
    left: 300px;
    top: 110px;
    width: 420px;
    height: 300px;
    background: radial-gradient(ellipse at center, var(--watermark-grey) 0%, rgba(223,224,226,0.55) 55%, rgba(223,224,226,0) 75%);
  }
  .card--back .watermark {
    left: 250px;
    top: 70px;
    width: 380px;
    height: 280px;
    background: radial-gradient(ellipse at center, var(--brand-blue-deep) 0%, rgba(26,85,150,0.6) 55%, rgba(26,85,150,0) 75%);
  }

  .brand {
    position: absolute;
    top: 70px;
    left: 70px;
    display: flex;
    align-items: center;
    gap: 16px;
  }
  .brand__dot {
    width: 34px;
    height: 34px;
    border-radius: 50%;
    background: var(--brand-blue);
  }
  .brand__name {
    font-size: 64px;
    font-weight: 400;
    color: var(--brand-blue);
    letter-spacing: 1px;
    line-height: 1;
  }

  .company-details {
    position: absolute;
    right: 70px;
    bottom: 60px;
    text-align: right;
    font-style: normal;
    font-size: 25px;
    line-height: 1.45;
    color: var(--ink);
  }
  .company-details .label { font-weight: 700; }
  .company-details .web { color: var(--brand-blue); font-weight: 700; }

  .person-details {
    position: absolute;
    left: 330px;
    top: 330px;
    color: var(--ink-light);
    font-size: 27px;
    line-height: 1.35;
  }
  .person-details .person-name {
    font-size: 34px;
    font-weight: 400;
  }
  .person-details .person-name strong { font-weight: 700; }
</style>
</head>
<body>
<main class="sheet">
  <section class="card card--front" aria-label="Card front">
    <div class="watermark" role="img" aria-label="Faint grey brand watermark"></div>
    <div class="brand">
      <span class="brand__dot"></span>
      <span class="brand__name">Tallobrix</span>
    </div>
    <address class="company-details">
      <p><span class="label">ABN:</span> 52 683 914 207</p>
      <p>47-49 Pembury Street, Ashcombe Vale, Victoria 3172</p>
      <p><span class="label">P</span> 1300 GRAB UP &nbsp; <span class="label">F</span> 03 9417 6258</p>
      <p class="web">www.tallobrix.com.au</p>
    </address>
  </section>

  <section class="card card--back" aria-label="Card back">
    <div class="watermark" role="img" aria-label="Deep blue brand watermark"></div>
    <div class="person-details">
      <p class="person-name">Dana <strong>Whitlow</strong></p>
      <p>PHN-NUM-XXXX</p>
      <p>abc@tallobrix.com.au</p>
    </div>
  </section>
</main>
</body>
</html>
```